Kestrel Studio Wall Art Design

Our local government has developed a department called the "Kestrel Studio" which has been running for a few years. Our purpose is to encourage staff to think Marigold Corner and engage their problems in new ways. We offer tools and services which enable collaboration between people and other departments, one such tool is our new meeting room. We've designed this space with the intention of encouraging creativity and allowing staff members to break away from the ordinary working environment. Attached are photos of the room.
The room is called "Marigold Corner". In one photo you will see our Marigold Corner sign filling the space where'd we'd like to have the design on, however we would like to stay away from naming labels in our design to convey to staff that this is their space as well, rather than the Kestrel Studio's special little room. We would like a design that embodies the spirit of our department. We've talked about what that means to us and we've stepped it out as;
Investigate
Collaborate
Innovate
Create
Celebrate
We had ideas of having a funky word jumble design or something creative to use these words, but we'd love to see anything else that conveys a feeling of creativity.
The size of the art is limited to 1400mm x 2800mm

```html
<!DOCTYPE html>
<html lang="en">
<head>
<meta charset="utf-8">
<title>Kestrel Studio – Wall Art</title>
<link rel="stylesheet" href="https://fonts.googleapis.com/css2?family=Archivo+Black&display=swap">
<style>
  :root {
    --band-grey: #f4f4f4;
    --band-white: #ffffff;
    --letter-outline: #2a2a2a;

    --shell-cream: #f1ebe4;
    --shell-pearl: #cfc8c4;
    --shell-amber: #c0783a;
    --shell-rust: #a9561f;

    --scale-teal: #79c9a9;
    --scale-mint: #9fd8bf;
    --scale-lime: #9cc43a;
    --scale-gold: #e2b411;

    --plume-lime: #b9d84a;
    --plume-green: #5f9a2a;
    --plume-copper: #b8774a;
    --plume-shadow: #1f3312;

    --wing-royal: #3b63d6;
    --wing-sky: #7c9ef0;
    --wing-deep: #142a7a;

    --night-navy: #0d1a3a;
    --night-ink: #050b1c;
    --night-flash: #6f9cff;
  }

  html, body {
    margin: 0;
    padding: 0;
    width: 1200px;
    height: 1074px;
    overflow: hidden;
    background: var(--band-grey);
  }

  .wall-art {
    display: block;
    width: 1200px;
    height: 1074px;
  }

  .band--grey { fill: var(--band-grey); }
  .band--white { fill: var(--band-white); }

  .value-word {
    font-family: "Archivo Black", "Arial Black", sans-serif;
    stroke: var(--letter-outline);
    stroke-width: 1;
    paint-order: stroke fill;
  }

  .shell-cream { stop-color: var(--shell-cream); }
  .shell-pearl { stop-color: var(--shell-pearl); }
  .shell-amber { stop-color: var(--shell-amber); }
  .shell-rust { stop-color: var(--shell-rust); }

  .scale-teal { stop-color: var(--scale-teal); }
  .scale-mint { stop-color: var(--scale-mint); }
  .scale-lime { stop-color: var(--scale-lime); }
  .scale-gold { stop-color: var(--scale-gold); }

  .plume-lime { stop-color: var(--plume-lime); }
  .plume-green { stop-color: var(--plume-green); }
  .plume-copper { stop-color: var(--plume-copper); }
  .plume-shadow { stop-color: var(--plume-shadow); }

  .wing-royal { stop-color: var(--wing-royal); }
  .wing-sky { stop-color: var(--wing-sky); }
  .wing-deep { stop-color: var(--wing-deep); }

  .night-navy { stop-color: var(--night-navy); }
  .night-ink { stop-color: var(--night-ink); }
  .night-flash { stop-color: var(--night-flash); }
</style>
</head>
<body>
<svg class="wall-art" viewBox="0 0 1200 1074" xmlns="http://www.w3.org/2000/svg">
  <defs>
    <linearGradient id="fill-shell" gradientUnits="userSpaceOnUse" x1="229" y1="0" x2="1021" y2="0">
      <stop offset="0" class="shell-pearl"/>
      <stop offset="0.08" class="shell-rust"/>
      <stop offset="0.16" class="shell-cream"/>
      <stop offset="0.3" class="shell-amber"/>
      <stop offset="0.42" class="shell-cream"/>
      <stop offset="0.55" class="shell-pearl"/>
      <stop offset="0.7" class="shell-cream"/>
      <stop offset="0.82" class="shell-rust"/>
      <stop offset="0.92" class="shell-cream"/>
      <stop offset="1" class="shell-pearl"/>
    </linearGradient>

    <linearGradient id="fill-scales" gradientUnits="userSpaceOnUse" x1="89" y1="0" x2="1110" y2="0">
      <stop offset="0" class="scale-lime"/>
      <stop offset="0.12" class="scale-teal"/>
      <stop offset="0.3" class="scale-mint"/>
      <stop offset="0.42" class="scale-teal"/>
      <stop offset="0.5" class="scale-gold"/>
      <stop offset="0.6" class="scale-mint"/>
      <stop offset="0.7" class="scale-gold"/>
      <stop offset="0.8" class="scale-lime"/>
      <stop offset="0.9" class="scale-teal"/>
      <stop offset="1" class="scale-mint"/>
    </linearGradient>

    <linearGradient id="fill-plume" gradientUnits="userSpaceOnUse" x1="75" y1="530" x2="1120" y2="640">
      <stop offset="0" class="plume-shadow"/>
      <stop offset="0.08" class="plume-lime"/>
      <stop offset="0.3" class="plume-lime"/>
      <stop offset="0.45" class="plume-copper"/>
      <stop offset="0.55" class="plume-green"/>
      <stop offset="0.62" class="plume-shadow"/>
      <stop offset="0.7" class="plume-copper"/>
      <stop offset="0.82" class="plume-lime"/>
      <stop offset="0.9" class="plume-green"/>
      <stop offset="1" class="plume-lime"/>
    </linearGradient>

    <linearGradient id="fill-wing" gradientUnits="userSpaceOnUse" x1="56" y1="0" x2="1139" y2="0">
      <stop offset="0" class="wing-deep"/>
      <stop offset="0.12" class="wing-royal"/>
      <stop offset="0.22" class="wing-sky"/>
      <stop offset="0.3" class="wing-deep"/>
      <stop offset="0.45" class="wing-royal"/>
      <stop offset="0.55" class="wing-sky"/>
      <stop offset="0.7" class="wing-royal"/>
      <stop offset="0.85" class="wing-sky"/>
      <stop offset="1" class="wing-royal"/>
    </linearGradient>

    <linearGradient id="fill-night" gradientUnits="userSpaceOnUse" x1="56" y1="0" x2="1150" y2="0">
      <stop offset="0" class="night-ink"/>
      <stop offset="0.1" class="night-flash"/>
      <stop offset="0.18" class="night-navy"/>
      <stop offset="0.35" class="night-ink"/>
      <stop offset="0.45" class="night-navy"/>
      <stop offset="0.6" class="night-ink"/>
      <stop offset="0.72" class="night-flash"/>
      <stop offset="0.8" class="night-navy"/>
      <stop offset="0.92" class="night-flash"/>
      <stop offset="1" class="night-ink"/>
    </linearGradient>
  </defs>

  <rect class="band band--grey" x="0" y="0" width="1200" height="215"/>
  <rect class="band band--white" x="0" y="215" width="1200" height="301"/>
  <rect class="band band--grey" x="0" y="516" width="1200" height="558"/>

  <g role="img" aria-label="Value words filled with close-up nature textures: seashell, reptile scales, peacock feather and butterfly wing">
    <text class="value-word value-word--create" x="229" y="201" font-size="167"
          textLength="792" lengthAdjust="spacingAndGlyphs" fill="url(#fill-shell)">CREATE</text>
    <text class="value-word value-word--innovate" x="89" y="424" font-size="164"
          textLength="1021" lengthAdjust="spacingAndGlyphs" fill="url(#fill-scales)">INNOVATE</text>
    <text class="value-word value-word--celebrate" x="75" y="637" font-size="146"
          textLength="1045" lengthAdjust="spacingAndGlyphs" fill="url(#fill-plume)">CELEBRATE</text>
    <text class="value-word value-word--collaborate" x="56" y="814" font-size="121"
          textLength="1083" lengthAdjust="spacingAndGlyphs" fill="url(#fill-wing)">COLLABORATE</text>
    <text class="value-word value-word--investigate" x="56" y="970" font-size="132"
          textLength="1094" lengthAdjust="spacingAndGlyphs" fill="url(#fill-night)">INVESTIGATE</text>
  </g>
</svg>
</body>
</html>
```